Modern Business Card for Lanternfield 2018

Our company assumes the best about people. We are creating an online community of entrepreneurs and business leaders who struggle with marketing their business online.

This business card should POP! We recently got a new logo and are launching a new website next month, so our business cards should make a statement that feels:
-Fresh
-Smart
-Trustworthy
-Fun

Target Market(s)

small business owners, entrepreneurs

Industry/Entity Type

Digital Marketing

Contact Information for Business Card

Dimensions: 3.5" x 2"

Font styles to use
Sans Serif

Colors
f37122
ffffff

Requirements
Must have
• We need a business card with a modern, bold design. We will use one side of the card as a lead-generation offer, so text on one side will need to fit up to 140 characters. The business card should stick to our core colors (orange, black, and white).
Nice to have
• We think a vertical "portrait" design could be interesting.
Should not have
• Should not look like a traditional business card. The round icon should stand out from a distance.

```html
<!DOCTYPE html>
<html lang="en">
<head>
<meta charset="utf-8">
<title>Lanternfield Business Card</title>
<link rel="stylesheet" href="https://fonts.googleapis.com/css2?family=Montserrat:wght@300;400;600;700;800&family=Caveat+Brush&family=Caveat:wght@500&display=swap">
<style>
  :root {
    --orange: #f37122;
    --black: #231f20;
    --charcoal: #2b2b2b;
    --white: #ffffff;
    --peach: #fdeee4;
    --backdrop: #e6e6e6;
  }
  * { margin: 0; padding: 0; box-sizing: border-box; }
  html, body { width: 1200px; height: 930px; overflow: hidden; }
  body {
    background: var(--backdrop);
    position: relative;
    font-family: "Montserrat", sans-serif;
  }

  /* Front: personal side */
  .card-front {
    position: absolute;
    left: 90px; top: 305px;
    width: 560px; height: 320px;
    border-radius: 22px;
    overflow: hidden;
    background: var(--white);
    box-shadow: 0 10px 30px rgba(0,0,0,.18);
  }
  .card-front .pattern-field {
    position: absolute; inset: 0;
    background: radial-gradient(circle at 50% 50%, var(--white) 0%, var(--peach) 100%);
  }
  .card-front .identity {
    position: absolute; left: 0; right: 0; top: 96px;
    text-align: center;
  }
  .card-front .person-name {
    font-family: "Caveat Brush", cursive;
    font-size: 62px; line-height: 1;
    color: var(--orange);
    letter-spacing: 2px;
  }
  .card-front .person-role {
    margin-top: 6px;
    font-weight: 800; font-size: 19px;
    letter-spacing: 1px;
    color: var(--black);
  }
  .card-front .email {
    position: absolute; right: 38px; bottom: 34px;
    font-weight: 600; font-size: 15px;
    color: var(--black);
  }

  /* Back: lead-generation side */
  .card-back {
    position: absolute;
    left: 770px; top: 185px;
    width: 320px; height: 560px;
    border-radius: 22px;
    overflow: hidden;
    background: var(--orange);
    box-shadow: 0 10px 30px rgba(0,0,0,.18);
    color: var(--white);
  }
  .card-back .top-band {
    position: absolute; left: 0; right: 0; top: 0; height: 58px;
    background: var(--charcoal);
  }
  .card-back .bottom-panel {
    position: absolute; left: 0; right: 0; bottom: 0; height: 96px;
    background: var(--white);
  }
  .card-back .bottom-edge {
    position: absolute; left: 0; right: 0; bottom: 0; height: 14px;
    background: var(--orange);
  }
  .card-back .content {
    position: absolute; left: 28px; right: 28px; top: 78px;
  }
  .brand {
    display: flex; align-items: center; gap: 10px;
  }
  .brand-dot {
    width: 30px; height: 30px; border-radius: 50%;
    background: var(--white); flex: none;
  }
  .brand-name {
    font-weight: 700; font-size: 27px; letter-spacing: .5px;
  }
  .tagline {
    margin-top: 6px;
    font-family: "Caveat", cursive;
    font-size: 17px; letter-spacing: .5px;
  }
  .divider { display: block; margin: 14px 0; }
  .promise {
    font-weight: 800; font-size: 21px; line-height: 1.2;
    text-transform: uppercase;
  }
  .offer {
    font-weight: 300; font-size: 17px; line-height: 1.3;
  }
  .offer-link {
    margin-top: 4px;
    font-weight: 700; font-size: 17px;
  }
</style>
</head>
<body>
  <section class="card-front" aria-label="Business card, personal side">
    <div class="pattern-field" role="img" aria-label="Faint repeating brand-mark pattern in soft peach"></div>
    <div class="identity">
      <div class="person-name">DANA WHITLOCK</div>
      <div class="person-role">STORY MARKETING COACH</div>
    </div>
    <div class="email">dana@lanternfieldnow.com</div>
  </section>

  <section class="card-back" aria-label="Business card, offer side">
    <div class="top-band"></div>
    <div class="content">
      <div class="brand">
        <span class="brand-dot"></span>
        <span class="brand-name">LANTERNFIELD</span>
      </div>
      <div class="tagline">Tell stories that inspire action</div>
      <svg class="divider" width="264" height="10" viewBox="0 0 264 10">
        <line x1="40" y1="5" x2="122" y2="5" stroke="#fff" stroke-width="1"/>
        <circle cx="132" cy="5" r="3" fill="#fff"/>
        <line x1="142" y1="5" x2="224" y2="5" stroke="#fff" stroke-width="1"/>
      </svg>
      <div class="promise">
        Reach more people.<br>
        Make more money.<br>
        Create more impact.
      </div>
      <svg class="divider" width="264" height="10" viewBox="0 0 264 10">
        <line x1="40" y1="5" x2="122" y2="5" stroke="#fff" stroke-width="1"/>
        <circle cx="132" cy="5" r="3" fill="#fff"/>
        <line x1="142" y1="5" x2="224" y2="5" stroke="#fff" stroke-width="1"/>
      </svg>
      <p class="offer">Get your free Lanternfield Starter Package and our marketing guide today at</p>
      <p class="offer-link">lanternfieldnow.com/start</p>
    </div>
    <div class="bottom-panel"></div>
    <div class="bottom-edge"></div>
  </section>
</body>
</html>
```